Bref créative
Logo for a homebuyer business
Brightkey Dwellings Homebuyers
Use same font as used in my logo
Miriam Colby
Co-Owner
xxxxx
BrightKeyDwellings@mailbox-example.net
BrightKeyDwellings.example

```html
<!DOCTYPE html>
<html lang="en">
<head>
<meta charset="utf-8">
<title>Brightkey Dwellings Homebuyers – Business Card</title>
<link href="https://fonts.googleapis.com/css2?family=Cinzel:wght@600&family=Open+Sans:wght@400;600&display=swap" rel="stylesheet">
<style>
  :root {
    --backdrop: #d6d7d9;
    --card: #ffffff;
    --navy: #2c3a92;
    --bronze: #8b5d3f;
    --ink: #3a3f4f;
  }
  html, body {
    margin: 0;
    width: 1200px;
    height: 895px;
    overflow: hidden;
    background: var(--backdrop);
  }
  .card {
    position: absolute;
    left: 100px;
    top: 162px;
    width: 1000px;
    height: 572px;
    background: var(--card);
    box-shadow: 0 6px 24px rgba(0,0,0,0.15);
  }
  .brand {
    position: absolute;
    top: 92px;
    left: 0;
    width: 100%;
    display: flex;
    justify-content: center;
    align-items: center;
    gap: 18px;
  }
  .brand-dot {
    width: 22px;
    height: 22px;
    border-radius: 50%;
    background: var(--navy);
  }
  .brand-name {
    font-family: "Cinzel", serif;
    font-weight: 600;
    color: var(--navy);
    font-size: 40px;
    line-height: 1.15;
    text-align: center;
    letter-spacing: 1px;
  }
  .band-rule {
    position: absolute;
    left: 0;
    width: 100%;
    height: 4px;
    background: var(--bronze);
  }
  .band-rule.top { top: 300px; }
  .band-rule.bottom { top: 384px; }
  .band {
    position: absolute;
    left: 0;
    top: 310px;
    width: 100%;
    height: 68px;
    background: var(--navy);
    display: flex;
    align-items: center;
    justify-content: center;
    font-family: "Open Sans", sans-serif;
    color: #fff;
    font-size: 28px;
  }
  .band .person { font-weight: 600; }
  .band .divider { margin: 0 16px; }
  .contacts {
    position: absolute;
    top: 420px;
    left: 90px;
    right: 90px;
    display: grid;
    grid-template-columns: 1fr 1.4fr;
    row-gap: 22px;
    column-gap: 40px;
    font-family: "Open Sans", sans-serif;
    font-size: 22px;
    color: var(--ink);
  }
  .contact {
    display: flex;
    align-items: center;
    gap: 12px;
    white-space: nowrap;
  }
  .contact svg { flex: none; }
</style>
</head>
<body>
  <div class="card">
    <div class="brand">
      <span class="brand-dot"></span>
      <div class="brand-name">Brightkey Dwellings<br>Homebuyers</div>
    </div>

    <div class="band-rule top"></div>
    <div class="band">
      <span class="person">Miriam Colby</span><span class="divider">|</span><span class="role">Co-Owner</span>
    </div>
    <div class="band-rule bottom"></div>

    <div class="contacts">
      <div class="contact">
        <svg width="26" height="26" viewBox="0 0 26 26"><circle cx="13" cy="13" r="13" fill="#2c3a92"/><path d="M9 7l3 3-1.5 1.5c.8 1.7 2.3 3.2 4 4L16 14l3 3-2 2c-4.5-.5-8.5-4.5-9-9z" fill="#fff"/></svg>
        <span>555-010-2040</span>
      </div>
      <div class="contact">
        <svg width="26" height="26" viewBox="0 0 26 26"><circle cx="13" cy="13" r="13" fill="#2c3a92"/><path d="M9 7l3 3-1.5 1.5c.8 1.7 2.3 3.2 4 4L16 14l3 3-2 2c-4.5-.5-8.5-4.5-9-9z" fill="#fff"/></svg>
        <span>(555) 014-3388</span>
      </div>
      <div class="contact">
        <svg width="26" height="26" viewBox="0 0 26 26"><circle cx="13" cy="13" r="13" fill="#2c3a92"/><circle cx="13" cy="13" r="7" fill="none" stroke="#fff" stroke-width="1.6"/><path d="M6 13h14M13 6c-3 4-3 10 0 14M13 6c3 4 3 10 0 14" fill="none" stroke="#fff" stroke-width="1.3"/></svg>
        <span>www.BrightKeyDwellings.example</span>
      </div>
      <div class="contact">
        <svg width="26" height="26" viewBox="0 0 26 26"><circle cx="13" cy="13" r="13" fill="#2c3a92"/><rect x="7" y="9" width="12" height="9" fill="none" stroke="#fff" stroke-width="1.6"/><path d="M7 9l6 5 6-5" fill="none" stroke="#fff" stroke-width="1.6"/></svg>
        <span>BrightKeyDwellings@mailbox-example.net</span>
      </div>
    </div>
  </div>
</body>
</html>
```